" Minha empresa basicamente funciona da seguinte forma, visito os clientes, pego todas as ideias (Briefing), levo para a empresa, elaboramos o melhor projeto possivel para aquele cliente, apresentamos o projeto, o cliente aprovando, começamos a fabricação. E estamos sempre envolvidos em eventos para trazer tecnologia para nossos clientes. "

```html
<!DOCTYPE html>
<html lang="pt-BR">
<head>
<meta charset="utf-8">
<title>Velmonti – Papel Timbrado</title>
<link href="https://fonts.googleapis.com/css2?family=Montserrat:wght@400;500;600&display=swap" rel="stylesheet">
<style>
  :root {
    --backdrop: #e4e4e4;
    --paper: #ffffff;
    --brown-dark: #3d2b22;
    --brown-mid: #8c7260;
    --sand: #bfa88f;
    --text-muted: #7d6a5c;
    --watermark: #f4f4f4;
  }
  * { margin: 0; padding: 0; box-sizing: border-box; }
  html, body {
    width: 1200px; height: 1200px; overflow: hidden;
    background: var(--backdrop);
    font-family: "Montserrat", sans-serif;
  }
  .letterhead {
    position: absolute;
    left: 212px; top: 50px;
    width: 776px; height: 1100px;
    background: var(--paper);
    box-shadow: 0 12px 40px rgba(0,0,0,0.18);
    overflow: hidden;
  }
  .top-rule {
    position: absolute; left: 0; top: 0;
    width: 100%; height: 12px;
    background: var(--brown-dark);
  }
  .brand {
    position: absolute; top: 72px; left: 0; width: 100%;
    text-align: center;
  }
  .brand-mark {
    display: block; width: 34px; height: 34px;
    margin: 0 auto 10px;
    background: var(--brown-mid);
  }
  .brand-name {
    font-size: 40px; font-weight: 500; letter-spacing: 3px;
    color: var(--brown-mid); line-height: 1;
  }
  .brand-tagline {
    margin-top: 6px;
    font-size: 10px; font-weight: 500; letter-spacing: 5px;
    color: var(--brown-mid);
  }
  .brand-site {
    margin-top: 14px;
    font-size: 13px; color: var(--sand);
  }
  .watermark {
    position: absolute;
    left: 168px; top: 270px;
    width: 440px; height: 440px;
    border-radius: 50%;
    background: var(--watermark);
  }
  .contact-line {
    position: absolute; right: 70px; bottom: 118px;
    display: flex; gap: 34px;
    font-size: 14px; font-weight: 500; color: var(--text-muted);
  }
  .contact-item { display: flex; align-items: center; gap: 10px; }
  .contact-item svg { width: 22px; height: 22px; }
  .footer-band {
    position: absolute; left: 0; bottom: 0;
    width: 100%; height: 86px;
    background: var(--sand);
    display: flex; align-items: center; justify-content: flex-end;
    padding-right: 70px;
    font-size: 15px; font-weight: 500; color: var(--paper);
  }
</style>
</head>
<body>
  <main class="letterhead">
    <div class="top-rule"></div>

    <header class="brand">
      <span class="brand-mark"></span>
      <div class="brand-name">VELMONTI</div>
      <div class="brand-tagline">MÓVEIS PLANEJADOS</div>
      <div class="brand-site">www.velmonti.com.br</div>
    </header>

    <div class="watermark" role="img" aria-label="Marca d'água clara da empresa"></div>

    <div class="contact-line">
      <span class="contact-item">
        <svg viewBox="0 0 22 22" aria-hidden="true">
          <rect x="1" y="1" width="20" height="20" rx="3" fill="none" stroke="var(--text-muted)" stroke-width="1.5"/>
          <path d="M7 6 l2 0 l1 3 l-1.5 1 a6 6 0 0 0 3.5 3.5 l1-1.5 l3 1 l0 2 a1.5 1.5 0 0 1-1.5 1.5 a9 9 0 0 1-8-8 a1.5 1.5 0 0 1 1.5-1.5z" fill="var(--text-muted)"/>
        </svg>
        (11) 3456-0198
      </span>
      <span class="contact-item">
        <svg viewBox="0 0 22 22" aria-hidden="true">
          <rect x="1" y="1" width="20" height="20" rx="3" fill="none" stroke="var(--text-muted)" stroke-width="1.5"/>
          <rect x="5" y="7" width="12" height="8" fill="none" stroke="var(--text-muted)" stroke-width="1.3"/>
          <path d="M5 7 l6 5 l6-5" fill="none" stroke="var(--text-muted)" stroke-width="1.3"/>
        </svg>
        mail@velmonti.com.br
      </span>
    </div>

    <footer class="footer-band">Av. Lagoa Serena, 240 | Centro | Rio de Janeiro/RJ</footer>
  </main>
</body>
</html>
```